Guild for Stewardship in Civic Ventures Needs a Save the Date Flyer Design

We need a Save the Date for our 8th Annual GuSCV Forum on April 6-8, 2016.

We will be having a golf tournament on April 6 and Conference from April 7-8.

Our Mission is to: Evolve the Capital Projects Industry through sharing of knowledge for optimized leadership, delivery and performance.

The Forum Theme is: THRIVE

Flyer should be 1 page and aim to engage and pull people in to come to our annual conference.

Target Market(s)

Architects, Engineers, Contractors, Owners

Industry/Entity Type

Leadership

Requirements
Must have
• Name: 8th Annual GuSCV Forum
• Date: April 6-8, 2016
• Location: Marwood Hotel and Spa, San Antonio, TX
• Theme is: THRIVE
• Why thrive? Let's plan ahead and take advantage of this opportunistic time.
• Three key topics to include leadership, funding and budgets, and project delivery
• G-GuSCV Logo
• Website: g-guscv.example
• Contact Info: Denise Holtvedt
• Editable for sponsor and speaker request flyers.
• Graphics
Nice to have
• Graphics related to theme, topics, location and what our mission is.
• Sub Topics:
• Topic 1: Leadership
• Being a strong public client
• Strategic planning
• Staffing
• Topic 2: Funding and Budgets
• Bonds
• P3's
• Developing accurate project budgets and the art of prediction and contingencies
• Topic 3: Project delivery
• Choosing the best delivery method for today's realities and tomorrow's unknowns
• Key elements for a successful project
• IPD-ish and other trends

```html
<!DOCTYPE html>
<html lang="en">
<head>
<meta charset="utf-8">
<title>8th Annual GuSCV Forum – Save the Date</title>
<link href="https://fonts.googleapis.com/css2?family=Open+Sans:wght@400;600;700;800&display=swap" rel="stylesheet">
<style>
  :root{
    --green:#5aa02c;
    --green-dark:#3f7f1c;
    --blue:#1f6fb8;
    --blue-dark:#14508a;
    --grey-text:#6b6b6b;
    --dark-text:#2e2e2e;
    --white:#ffffff;
    --sky-top:#3d86c6;
    --sky-mid:#b9d9ee;
    --grass:#6fae3a;
  }
  *{margin:0;padding:0;box-sizing:border-box}
  html,body{width:887px;height:1200px;overflow:hidden;background:var(--white)}
  body{font-family:"Open Sans",Arial,sans-serif;position:relative;color:var(--dark-text)}
  .hero-scene{position:absolute;left:0;top:0;width:887px;height:800px;
    background:linear-gradient(180deg,var(--sky-top) 0%,var(--sky-mid) 40%,#e7f1f7 62%,#9cc76b 78%,var(--grass) 100%)}
  .hero-fade{position:absolute;left:0;top:90px;width:620px;height:360px;
    background:linear-gradient(90deg,rgba(255,255,255,.85),rgba(255,255,255,.55) 70%,rgba(255,255,255,0))}
  .brand{position:absolute;left:22px;top:14px;display:flex;align-items:center;gap:10px;
    color:var(--white);font-weight:800;font-size:34px;letter-spacing:.5px}
  .brand-mark{width:30px;height:30px;background:var(--white);border-radius:50%}
  .tagline{position:absolute;left:150px;top:116px;width:480px;color:var(--grey-text);
    font-size:24px;line-height:1.3;font-weight:400}
  .event-box{position:absolute;left:154px;top:205px;width:380px;height:190px;background:var(--green);
    color:var(--white);text-align:center;padding-top:20px}
  .event-name{font-size:27px;font-weight:600}
  .event-date{font-size:33px;font-weight:700;margin-top:4px}
  .event-venue{font-size:25px;font-weight:600;line-height:1.2;margin-top:4px}
  .topic-card{position:absolute;background:var(--white);box-shadow:0 3px 10px rgba(0,0,0,.3);overflow:hidden}
  .topic-leadership{left:104px;top:488px;width:227px;height:390px}
  .topic-funding{left:346px;top:430px;width:218px;height:448px}
  .topic-delivery{left:571px;top:430px;width:222px;height:448px}
  .topic-head{padding:12px 12px 8px}
  .topic-title{font-size:23px;font-weight:700;line-height:1.15}
  .topic-leadership .topic-title{color:var(--green);text-transform:uppercase}
  .topic-funding .topic-head{background:var(--white)}
  .topic-funding .topic-title{color:var(--dark-text);font-weight:600;text-align:center}
  .topic-delivery .topic-head{background:var(--blue);color:var(--white)}
  .topic-text{font-size:12px;line-height:1.45;margin-top:6px}
  .topic-leadership .topic-text,.topic-funding .topic-text{color:var(--grey-text)}
  .topic-photo{position:absolute;left:0;bottom:0;width:100%}
  .photo-team{height:250px;background:linear-gradient(180deg,#d9dde2,#8d939b 60%,#3f4650)}
  .photo-money{height:270px;background:linear-gradient(180deg,#bfe0f1,#8cc27a 55%,#5f8e3a)}
  .photo-clock{height:250px;background:linear-gradient(180deg,#d8c7a4,#a8875a 55%,#6d5436)}
  .cta{position:absolute;left:104px;top:894px;font-size:24px;line-height:1.3;color:var(--dark-text);width:380px}
  .cta strong{color:var(--green);font-weight:700}
  .call{position:absolute;left:476px;top:890px;color:var(--blue);font-size:30px;font-weight:700}
  .web{position:absolute;left:476px;top:934px;color:var(--blue);font-size:23px}
  .info-col{position:absolute;top:980px}
  .info-about{left:104px;width:330px}
  .info-why{left:476px;width:370px}
  .info-title{font-size:26px;font-weight:700;color:var(--dark-text)}
  .info-title span{color:var(--blue)}
  .info-body{margin-top:6px;font-size:14px;line-height:1.3;color:var(--grey-text);text-align:justify}
  .info-list{margin-top:6px;list-style:none;font-size:14px;line-height:1.3;color:var(--grey-text)}
  .footer-bar{position:absolute;left:0;top:1128px;width:887px;height:72px;
    background:linear-gradient(90deg,var(--blue-dark),var(--blue))}
  .footer-contact{position:absolute;left:104px;top:1150px;color:var(--white);font-size:22px;font-weight:600}
  .footer-brand{position:absolute;right:0;top:1112px;width:240px;height:88px;background:var(--white);
    border-top-left-radius:8px;display:flex;align-items:center;justify-content:center;gap:10px;
    color:var(--blue);font-weight:800;font-size:32px}
  .footer-brand .brand-mark{background:var(--blue)}
</style>
</head>
<body>
  <div class="hero-scene" role="img" aria-label="Businessman holding a glowing light bulb against a blue sky, city skyline and green lawn"></div>
  <div class="hero-fade"></div>

  <div class="brand"><span class="brand-mark"></span>G-GuSCV</div>

  <p class="tagline">Why thrive? Let’s plan ahead and take advantage of this opportunistic time</p>

  <div class="event-box">
    <p class="event-name">8th Annual GuSCV Forum</p>
    <p class="event-date">April 6-8, 2016</p>
    <p class="event-venue">Marwood Hotel and Spa,<br>San Antonio, TX</p>
  </div>

  <section class="topic-card topic-leadership">
    <div class="topic-head">
      <h2 class="topic-title">Leadership</h2>
      <p class="topic-text">Being a strong public client<br>Strategic planning, Staffing</p>
    </div>
    <div class="topic-photo photo-team" role="img" aria-label="Smiling business team in office attire"></div>
  </section>

  <section class="topic-card topic-funding">
    <div class="topic-head">
      <h2 class="topic-title">Funding and Budgets</h2>
      <p class="topic-text">Bonds, Developing accurate project budgets and the art of prediction and contingencies, P3's</p>
    </div>
    <div class="topic-photo photo-money" role="img" aria-label="Tree growing banknotes under a blue sky"></div>
  </section>

  <section class="topic-card topic-delivery">
    <div class="topic-head">
      <h2 class="topic-title">Project delivery</h2>
      <p class="topic-text">Key elements for a successful project Choosing the best delivery method for today's realities and tomorrow's unknowns</p>
    </div>
    <div class="topic-photo photo-clock" role="img" aria-label="Vintage pocket watch on a wooden surface"></div>
  </section>

  <p class="cta">Is not it time to <strong>get</strong><br><strong>professional help</strong> from a team?</p>
  <p class="call">Call Us : +123 456 78 90</p>
  <p class="web">www.g-guscv.example</p>

  <div class="info-col info-about">
    <h3 class="info-title">About Us <span>Company</span></h3>
    <p class="info-body">Wandis maharimur cekale ekale ilate dafuga keleats quisquaerum ium quatem voluptium laut alitust erares anem quam icus dut occus nonecto ritasperovit. Semit officiat daneesto</p>
  </div>

  <div class="info-col info-why">
    <h3 class="info-title">Why Choose Us?</h3>
    <ol class="info-list">
      <li>1. Dolorecti quo qitasperovi uam ise axim.</li>
      <li>2. Sam laboreperum voles aitasperovi enitas.</li>
      <li>3. Gitasper itasperovium quunti dolo captu.</li>
      <li>4. Moeleto tem dolup itasperovitaum evif.</li>
    </ol>
  </div>

  <div class="footer-bar"></div>
  <p class="footer-contact">Contact Info: Denise Holtvedt</p>
  <div class="footer-brand"><span class="brand-mark"></span>G-GuSCV</div>
</body>
</html>
```